I need professional letterhead for an attorney. I already have my logo (attached). I currently have a project going to get business cards. I would like the letterhead to be classy. It is very important that this letterhead be in a format that I can import it into Microsoft Word 2013. I plan on importing this into Word so I can type my documents directly onto it and electronically send the finished documents to my clients. Thank you very much.

Industry/Entity Type

Attorney

Requirements
Must have
• Here is my info. Please put it all on there:
• Dwight R. Mallory Attorney At Law
• 48613 Brackwell Crescent
• St. Louis, MO 63047
• Telephone: 314-596-2043
• Fax: 800-627-4915
• Email: Dwight@RivermarkWills.com
• Also, I need the ability to import this final design into Microsoft Word 2013 so that I can type directly onto it. I believe I can do that if you hand it over to me as a JPG and a PDF in addition to the other formats. Then I should be able to import it into Word.

```html
<!DOCTYPE html>
<html lang="en">
<head>
<meta charset="utf-8">
<title>Rivermark Wills Planning LLC – Letterhead</title>
<link rel="stylesheet" href="https://fonts.googleapis.com/css2?family=Tinos:wght@400&display=swap">
<style>
  :root {
    --brand-blue: #2f72b4;
    --accent-tint: #e6eef6;
    --rule-grey: #9a9a9a;
    --ink: #222222;
    --paper: #ffffff;
  }
  * { margin: 0; padding: 0; box-sizing: border-box; }
  html, body { width: 849px; height: 1200px; overflow: hidden; background: var(--paper); }
  .letterhead {
    position: relative;
    width: 849px;
    height: 1200px;
    background: var(--paper);
    font-family: "Tinos", "Times New Roman", serif;
    color: var(--ink);
    overflow: hidden;
  }
  .corner-accent {
    position: absolute;
    top: 0;
    right: 0;
    width: 160px;
    height: 300px;
  }
  .brand {
    position: absolute;
    top: 66px;
    left: 57px;
    display: flex;
    align-items: center;
    gap: 14px;
  }
  .brand-mark {
    width: 34px;
    height: 34px;
    background: var(--brand-blue);
    flex: none;
  }
  .brand-name {
    color: var(--brand-blue);
    font-weight: 400;
    font-size: 30px;
    line-height: 1;
    letter-spacing: 0;
    white-space: nowrap;
  }
  .footer {
    position: absolute;
    left: 42px;
    top: 1095px;
    width: 412px;
    border-top: 1px solid var(--rule-grey);
    padding: 16px 0 0 15px;
    display: flex;
    font-size: 11px;
    line-height: 15px;
  }
  .footer-block { font-style: normal; white-space: nowrap; }
  .footer-block span { display: block; }
  .footer-block.address { width: 218px; flex: none; }
</style>
</head>
<body>
  <div class="letterhead">
    <svg class="corner-accent" viewBox="0 0 160 300" aria-hidden="true">
      <circle cx="150" cy="120" r="140" fill="var(--accent-tint)"/>
    </svg>

    <header class="brand">
      <span class="brand-mark" aria-hidden="true"></span>
      <h1 class="brand-name">Rivermark Wills Planning LLC</h1>
    </header>

    <footer class="footer">
      <address class="footer-block address">
        <span>Dwight R. Mallory Attorney At Law</span>
        <span>48613 Brackwell Crescent</span>
        <span>St. Louis, MO 63047</span>
      </address>
      <address class="footer-block contact">
        <span>Telephone: 314-596-2043</span>
        <span>Fax: 800-627-4915</span>
        <span>Email: Dwight@RivermarkWills.com</span>
      </address>
    </footer>
  </div>
</body>
</html>
```